Business card for auto dealership

Looking for a clean modern design.
Would like attached logo incorporated

Industry/Entity Type

Car dealership

Contact Information for Business Card

Name, website, phone, cell, fax, email

```html
<!DOCTYPE html>
<html lang="en">
<head>
<meta charset="utf-8">
<title>Whitford Truck &amp; Auto Sales — Business Card</title>
<link rel="stylesheet" href="https://fonts.googleapis.com/css2?family=Open+Sans:wght@300;400;700&display=swap">
<style>
  :root {
    --stage: #dcdcdc;
    --card: #0b0b0b;
    --card-sheen: #2a2a2a;
    --ink: #ffffff;
    --ink-soft: #cfcfcf;
    --accent: #ffffff;
  }
  * { margin: 0; padding: 0; box-sizing: border-box; }
  html, body { width: 1200px; height: 876px; overflow: hidden; }
  body {
    background: var(--stage);
    font-family: "Open Sans", Arial, sans-serif;
    position: relative;
  }
  .card {
    position: absolute;
    top: 283px;
    width: 540px;
    height: 310px;
    background: radial-gradient(ellipse at 45% 35%, var(--card-sheen) 0%, var(--card) 70%);
    color: var(--ink);
    overflow: hidden;
    box-shadow: 0 8px 18px rgba(0,0,0,0.35);
  }
  .card--front { left: 40px; }
  .card--back { left: 620px; }

  .person { position: absolute; left: 36px; top: 30px; }
  .person__name { font-size: 30px; font-weight: 300; letter-spacing: 0.3px; line-height: 1.1; }
  .person__role { font-size: 11px; font-weight: 400; color: var(--ink-soft); margin-top: 2px; }

  .contact { position: absolute; left: 36px; font-size: 11.5px; display: flex; gap: 28px; white-space: nowrap; }
  .contact--address { top: 112px; }
  .contact--phones { top: 138px; }
  .contact--online { top: 222px; }
  .contact__item { display: flex; align-items: center; gap: 6px; }
  .icon { width: 11px; height: 11px; fill: var(--ink); flex: none; }

  .brand {
    position: absolute;
    font-weight: 700;
    font-size: 16px;
    line-height: 1.2;
    color: var(--ink);
    white-space: nowrap;
    display: flex;
    align-items: center;
    gap: 8px;
  }
  .brand__dot { width: 10px; height: 10px; background: var(--ink); border-radius: 50%; }
  .card--front .brand { right: 36px; top: 176px; }
  .card--back .brand { left: 226px; top: 143px; }

  .bar { position: absolute; background: var(--accent); }
  .card--front .bar { right: 0; bottom: 28px; width: 200px; height: 40px; }
  .card--back .bar--long { left: 0; top: 136px; width: 206px; height: 34px; }
  .card--back .bar--short { right: 0; top: 136px; width: 40px; height: 34px; }
</style>
</head>
<body>
  <section class="card card--front" aria-label="Business card front">
    <div class="person">
      <div class="person__name">Dana Whitford</div>
      <div class="person__role">owner</div>
    </div>

    <div class="contact contact--address">
      <span class="contact__item">
        <svg class="icon" viewBox="0 0 12 12"><path d="M6 0a4 4 0 0 0-4 4c0 3 4 8 4 8s4-5 4-8a4 4 0 0 0-4-4zm0 5.5A1.5 1.5 0 1 1 6 2.5a1.5 1.5 0 0 1 0 3z"/></svg>
        4120 Route 9 Millbrook, NY 12545, United States
      </span>
    </div>

    <div class="contact contact--phones">
      <span class="contact__item">
        <svg class="icon" viewBox="0 0 12 12"><path d="M2.5 0l2 3-1.2 1.2a7 7 0 0 0 4.5 4.5L9 7.5l3 2-1 2.5C5 12 0 7 0 1z"/></svg>
        555-014-2201
      </span>
      <span class="contact__item">
        <svg class="icon" viewBox="0 0 12 12"><path d="M3 0h6v12H3zM4 1v8h4V1z"/></svg>
        555-014-2202
      </span>
      <span class="contact__item">
        <svg class="icon" viewBox="0 0 12 12"><path d="M3 0h6v3h2v7H1V3h2zm1 1v2h4V1zM3 6v2h6V6z"/></svg>
        555-014-2203
      </span>
    </div>

    <div class="contact contact--online">
      <span class="contact__item">
        <svg class="icon" viewBox="0 0 12 12"><path d="M0 2h12v8H0zm1 1v.5l5 3 5-3V3z"/></svg>
        dana@whitfordauto.com
      </span>
      <span class="contact__item">
        <svg class="icon" viewBox="0 0 12 12"><path d="M6 0a6 6 0 1 0 0 12A6 6 0 0 0 6 0zm0 1c.8 0 1.6 2 1.7 4.5H4.3C4.4 3 5.2 1 6 1zM4.3 6.5h3.4C7.6 9 6.8 11 6 11s-1.6-2-1.7-4.5zM1 6.5h2.3c0 1.5.3 2.9.7 3.8A5 5 0 0 1 1 6.5zm0-1a5 5 0 0 1 3-3.8c-.4.9-.7 2.3-.7 3.8zm7.7 1H11a5 5 0 0 1-3 3.8c.4-.9.7-2.3.7-3.8zm0-1c0-1.5-.3-2.9-.7-3.8a5 5 0 0 1 3 3.8z"/></svg>
        www.whitfordauto.com
      </span>
    </div>

    <div class="brand"><span class="brand__dot"></span>Whitford Truck &amp; Auto Sales</div>
    <div class="bar"></div>
  </section>

  <section class="card card--back" aria-label="Business card back">
    <div class="bar bar--long"></div>
    <div class="brand"><span class="brand__dot"></span>Whitford Truck &amp; Auto Sales</div>
    <div class="bar bar--short"></div>
  </section>
</body>
</html>
```